Warranty Card Design for Mattress Brand

We would like to design a warranty card for our mattresses,
it consists of 2 pages in one card (front and back) to be neatly showing our warranty details/text , our logo , our website, address and telephone clearly.

Target Market(s)

household

Font styles to use
Serif
Script

Colors
3277b5
33a6d7
85cae6
0492cd
3176b5
0355a3
85abd2
cee9f5
85acd3

Requirements
Must have
• a nice warranty logo
Nice to have
• a nice warranty logo with a neat text and clear layout, colors have to be related to the logo

```html
<!DOCTYPE html>
<html lang="en">
<head>
<meta charset="utf-8">
<title>Duskwell Warranty Card</title>
<link href="https://fonts.googleapis.com/css2?family=Open+Sans:wght@400;600;700&family=Cormorant+Garamond:wght@400;500&display=swap" rel="stylesheet">
<style>
  :root {
    --brand-blue: #4f72c0;
    --panel-blue: #6f9dd4;
    --bullet-blue: #0492cd;
    --ink: #1d1d1d;
    --tick: #2e9a3e;
    --cross: #d3302b;
    --seal-orange: #f07f1b;
    --paper: #ffffff;
    --stage: #eef1f5;
    --rule: #222222;
  }
  * { box-sizing: border-box; margin: 0; padding: 0; }
  html, body { width: 1200px; height: 1000px; overflow: hidden; }
  body {
    background: var(--stage);
    font-family: "Open Sans", sans-serif;
    color: var(--ink);
    position: relative;
  }
  .spread {
    position: absolute;
    left: 60px;
    width: 1080px;
    height: 440px;
    display: flex;
    box-shadow: 0 4px 14px rgba(0,0,0,.12);
  }
  .spread--outside { top: 40px; }
  .spread--inside { top: 520px; }
  .panel {
    width: 540px;
    height: 440px;
    position: relative;
    background: var(--paper);
  }
  .panel + .panel { border-left: 1px solid #d9dde3; }

  /* Back cover */
  .panel--back { background: var(--panel-blue); color: #fff; }
  .back-brand {
    position: absolute; left: 0; right: 0; top: 150px;
    text-align: center;
    font-weight: 600; font-size: 54px; letter-spacing: 1px;
    color: #fff;
  }
  .back-contact {
    position: absolute; left: 0; right: 0; bottom: 42px;
    text-align: center; color: #111; font-size: 14px; line-height: 1.5;
  }
  .back-contact .company { font-weight: 700; }

  /* Front cover */
  .front-brand {
    position: absolute; left: 0; right: 0; top: 140px;
    text-align: center;
    font-weight: 600; font-size: 66px; letter-spacing: 1px;
    color: var(--brand-blue);
  }
  .front-tagline {
    position: absolute; left: 0; right: 0; top: 238px;
    text-align: center;
    font-family: "Cormorant Garamond", serif;
    font-size: 24px; letter-spacing: 6px;
    color: var(--brand-blue);
  }
  .warranty-seal {
    position: absolute; left: 230px; top: 320px;
    width: 80px; height: 80px; border-radius: 50%;
    background: radial-gradient(circle, #fff 52%, var(--seal-orange) 53%, var(--seal-orange) 70%, #fff 71%, #fff 80%, #333 81%);
  }
  .front-rules {
    position: absolute; left: 0; right: 0; bottom: 38px;
    height: 5px; border-top: 2px solid var(--rule); border-bottom: 1px solid var(--rule);
  }

  /* Inside */
  .panel--intro { padding: 40px 34px 0 38px; }
  .panel--terms { padding: 34px 34px 0 30px; }
  .inside-heading { font-size: 16px; font-weight: 700; margin-bottom: 8px; }
  .intro-list { list-style: none; font-size: 13.5px; line-height: 1.45; }
  .intro-list li { position: relative; padding-left: 14px; margin-bottom: 4px; }
  .intro-list li::before {
    content: ""; position: absolute; left: 0; top: 6px;
    width: 8px; height: 8px; border-radius: 50%; background: var(--bullet-blue);
  }
  .terms-heading { font-size: 13.5px; font-weight: 700; margin: 0 0 3px; }
  .terms-list { list-style: none; font-size: 12px; line-height: 1.38; margin-bottom: 12px; }
  .terms-list li { position: relative; padding-left: 12px; }
  .terms-list li::before { position: absolute; left: 0; font-weight: 700; }
  .terms-list--covered li::before { content: "\2713"; color: var(--tick); }
  .terms-list--excluded li::before { content: "\2715"; color: var(--cross); }
  .record-table {
    border-top: 2px dashed var(--rule);
    padding-top: 6px;
    width: 100%;
    border-collapse: collapse;
    font-size: 12.5px; font-weight: 600;
  }
  .record-divider { border-top: 2px dashed var(--rule); margin-top: 2px; }
  .record-table th { text-align: center; padding: 6px 0; border-bottom: 1px solid var(--rule); font-weight: 600; }
  .record-table th + th, .record-table td + td { border-left: 1px solid var(--rule); }
  .record-table td { height: 44px; }
</style>
</head>
<body>

<section class="spread spread--outside" aria-label="Warranty card outside">
  <div class="panel panel--back">
    <div class="back-brand">Duskwell</div>
    <div class="back-contact">
      <p class="company">Hadid Faris and Sons</p>
      <p>Cedar Hill, Mill Road, Aley, Lebanon</p>
      <p>T: +961 1 555 014 &nbsp;|&nbsp; W: www.hadidfarisandsons.com</p>
    </div>
  </div>
  <div class="panel panel--front">
    <div class="front-brand">Duskwell</div>
    <div class="front-tagline">MATTRESSES &amp; PILLOWS</div>
    <div class="warranty-seal" role="img" aria-label="One year warranty seal"></div>
    <div class="front-rules"></div>
  </div>
</section>

<section class="spread spread--inside" aria-label="Warranty card inside">
  <div class="panel panel--intro">
    <h2 class="inside-heading">Congratulations on your new DUSKWELL Mattress.</h2>
    <ul class="intro-list">
      <li>We always strive to provide you with the most comfortable and healthy sleep by offering you the highest product quality and durability.</li>
      <li>Our company was awarded the ISO 9001 accreditation certificate for the quality of its Mattress Production.</li>
      <li>By implementing the ISO 9001 quality management system, we assure our customers that the products and the services we provide will meet their expectations.</li>
      <li>Our products are guaranteed against defects in workmanship and material.</li>
      <li>In case of defect, we shall repair or replace, at our discretion, the defective component.</li>
      <li>Please keep this card in a safe place. Should you face any problems, please contact us with this card and your proof of purchase.</li>
    </ul>
  </div>
  <div class="panel panel--terms">
    <h3 class="terms-heading">This limited Mattress Warranty applies to the following Defects:</h3>
    <ul class="terms-list terms-list--covered">
      <li>Coils or wires that are broken or piercing through fabric.</li>
      <li>Sagging, that measures 3cm or greater (being properly measured) only if the mattress has been continuously supported by appropriate and solid foundation</li>
    </ul>
    <h3 class="terms-heading">This limited Mattress Warranty does not cover the following:</h3>
    <ul class="terms-list terms-list--excluded">
      <li>Comfort preference</li>
      <li>Fabric Stains, soiling or burns</li>
      <li>Body impressions of less than 3cm</li>
      <li>Damage to the mattress due to abuse</li>
      <li>Bent Perimeter border rods due to moving or bending the mattress</li>
      <li>Size allowance of +/- 2cm</li>
      <li>Bed Bugs or Dust Mites</li>
      <li>Odor (As in any upholstery, new mattress may have odor that will fade with time)</li>
      <li>Latex and Memory Foam mattresses: normal change in softness and height in these materials with time. This does not affect the relieving quality of these mattresses</li>
      <li>Transportation and Inspection Costs</li>
    </ul>
    <div class="record-divider"></div>
    <table class="record-table">
      <tr><th>Serial Number</th><th>Warranty Period</th><th>Date</th></tr>
      <tr><td></td><td></td><td></td></tr>
    </table>
  </div>
</section>

</body>
</html>
```